Corevail health fitness personal training classes 8 week challenges

Corevail (aust) pty ltd is the business name I have only a Facebook page corevail Marla

I instruct 4 classes fitness classes a week and run 8 week challenges aprox 3-5 a year. I do personal training and write programs
These web sites are similar to what Iam looking for
Tess rowan 8 week program
Paula Venn
Roxanne finch

The above sites offer what I offer
Bonus is mine can be done online and in person which can be draining since I then take in a lot of emotional stuff and stories and excuses from clients

They get given training programs which is what I do written programs but I also give them physical training sessions as well

The purpose of this site?
My goal is to stay in the health and fitness industry however my body is physically, emotionally mentally exhausted.
I am torn because I love my job but 28 years later and with a few health issues I can't do it.
I must stop i need to stop due to
My health but I can't I worry about the loss of income and letting people down

So if I can set up a website and a online app, 8 week challenge or add to my collection of fitness DVDs and put them online where I can work from home

on my Facebook you can access my albums and advertising material

My main primary audience is females between 25-55 however I cater for everyone young old for unfit challenged etc

On my website or app these are the things I would want to cover

Everyday there would be a new inspirational logo
A short program they can do in the privacy of there home
My fitness DVD's and workout clothing on sale
Fitness programs on sale

I have an in in inbundance of information I can draw from of eg my 3 fitness DVDs, receipes, logos, inspirational quotes from my Facebook so stuff I have used before I am wanting to produce another DVD And complete my book I would love to add that to my products

Eye catching words
Weight loss (only because that gets people in straight away)
Fat burner (example I teach a abs thigh butt class Monday yes it's burns calories as much as the Fatburner class but uneducated people will go to the Fatburner just because of the name

Corevail

28 years experience ( I believe i have so much experience and stories to share I have the qualifications and awards that I have won but it's my passion and desire to help others I think this is why my business is a success.
Can this translate online ??

I have won fitness professional awards

I want people to connect with me and I want there first reaction to be of hope and courage and know that they can do this that real wow anything is possible
Corevail is about the member and I genuinely care Yhey are not just a number

​I want them to trust that I have the knowledge and experience
Online fitness programs
The selling of my fitness DVDs
Online 8 week programs
Recipes
Before and after photos
Client testimonials

Target Market(s)

Majority a females aged between 18-60 years old

Industry/Entity Type

Health And Wellness

Coding

Coded - Design and coding required

Number of Pages Required

1 page

Font styles to use
Serif
Script

Colors
f37122
faa54b
3c7bb8
33a6d7

Requirements
Must have
• Albums / files as below
• Client testimonials
• Before and after photos
• Selling products eg DVD's/ programs etc
Nice to have
• My aim is to take my business more into online so I can still offer all my services eg classes, programs, nutritional advice, one on one consultant,
• However have the bonus of doing it from home online.
• Also my body needs to physically slow down
Should not have
• Not sure on this question

```html
<!DOCTYPE html>
<html lang="en">
<head>
<meta charset="utf-8">
<title>Corevail – Personal Training Centre</title>
<link href="https://fonts.googleapis.com/css2?family=Dancing+Script:wght@400;600&family=Noto+Serif:ital,wght@0,400;0,700;1,400&display=swap" rel="stylesheet">
<style>
:root{
  --orange:#f37122;
  --orange-soft:#faa54b;
  --blue-deep:#3c7bb8;
  --blue:#33a6d7;
  --ink:#333;
  --muted:#555;
  --white:#fff;
  --footer-bg:#f4f4f4;
  --script:'Dancing Script',cursive;
  --serif:'Noto Serif',Georgia,serif;
}
*{margin:0;padding:0;box-sizing:border-box}
html,body{width:1200px;height:3495px;overflow:hidden;background:var(--white)}
body{font-family:var(--serif);color:var(--ink);position:relative}
.photo{position:absolute}

/* header */
.site-header{position:absolute;top:0;left:0;width:1200px;height:105px;background:var(--white)}
.brand{position:absolute;left:77px;top:20px;display:flex;align-items:center;gap:10px}
.brand-mark{width:16px;height:16px;border-radius:50%;background:var(--orange)}
.brand-name{font-family:var(--serif);font-weight:700;font-size:40px;color:var(--blue-deep);letter-spacing:1px;line-height:1}
.brand-tag{position:absolute;left:105px;top:66px;font-size:11px;color:var(--muted)}
.main-nav{position:absolute;right:82px;top:38px;display:flex;gap:26px;font-size:16px}
.main-nav a{color:var(--ink);text-decoration:none}
.main-nav a.active{color:var(--orange)}

/* hero */
.hero{position:absolute;top:105px;left:0;width:1200px;height:573px;overflow:hidden}
.hero-photo{inset:0;background:
  radial-gradient(ellipse 260px 300px at 820px 140px,#e9c8a6 0%,rgba(233,200,166,0) 70%),
  radial-gradient(ellipse 300px 200px at 760px 470px,#f2e25a 0%,rgba(242,226,90,0) 70%),
  radial-gradient(ellipse 260px 260px at 1080px 420px,#e4588a 0%,rgba(228,88,138,0) 70%),
  radial-gradient(ellipse 240px 300px at 420px 380px,#9a74b8 0%,rgba(154,116,184,0) 70%),
  radial-gradient(ellipse 300px 240px at 1050px 120px,#d97aa0 0%,rgba(217,122,160,0) 70%),
  linear-gradient(100deg,#ece7e3 0%,#e3d6d2 30%,#cdb0a8 55%,#b89393 80%,#a88a8c 100%)}
.hero-veil{inset:0;background:linear-gradient(90deg,rgba(255,255,255,.72) 0%,rgba(255,255,255,.45) 35%,rgba(255,255,255,0) 55%)}
.hero-name{position:absolute;left:77px;top:118px;font-family:var(--script);font-size:72px;color:#111;line-height:1.2}
.hero-title{position:absolute;left:77px;top:210px;font-size:44px;color:#111;line-height:1.2}
.hero-sub{position:absolute;left:77px;top:268px;font-size:32px;line-height:46px;color:#111;width:520px}
.btn-outline{position:absolute;left:77px;top:389px;width:252px;height:65px;border:3px solid #111;display:flex;align-items:center;justify-content:center;font-size:19px;color:#111;background:rgba(255,255,255,.2)}

/* about */
.section-title{font-family:var(--script);color:var(--orange);font-weight:400}
.about-title{position:absolute;left:77px;top:725px;font-size:44px}
.about-text{position:absolute;left:77px;top:790px;width:490px;font-size:14.5px;line-height:27px;color:var(--muted)}
.btn-blue{position:absolute;left:77px;top:969px;width:166px;height:52px;background:var(--blue);color:var(--white);display:flex;align-items:center;justify-content:center;font-size:18px}
.video{left:622px;top:729px;width:499px;height:292px;background:
  radial-gradient(ellipse 200px 80px at 280px 200px,#3a3036 0%,rgba(58,48,54,0) 70%),
  radial-gradient(ellipse 160px 120px at 100px 60px,#a7b8c8 0%,rgba(167,184,200,0) 70%),
  linear-gradient(180deg,#8e98a6 0%,#6e7886 45%,#2b333c 70%,#1b2026 100%)}
.play{position:absolute;left:226px;top:122px}

/* programmes */
.programs{position:absolute;top:1074px;left:0;width:1200px;height:324px}
.program{position:absolute;top:0;width:300px;text-align:center}
.program .photo{position:relative;width:300px;height:198px}
.p1{background:radial-gradient(ellipse 90px 100px at 200px 100px,#e7c79c 0%,rgba(231,199,156,0) 70%),linear-gradient(180deg,#b58a66 0%,#9c7558 50%,#5f4a3f 100%)}
.p2{background:radial-gradient(ellipse 80px 110px at 140px 110px,#7a5b4e 0%,rgba(122,91,78,0) 70%),linear-gradient(180deg,#efe3d2 0%,#d8c2a6 55%,#a88c72 100%)}
.p3{background:radial-gradient(ellipse 70px 90px at 90px 90px,#e3c38e 0%,rgba(227,195,142,0) 70%),linear-gradient(180deg,#c7b8a5 0%,#9e8f7f 50%,#5a5048 100%)}
.p4{background:radial-gradient(ellipse 90px 80px at 200px 70px,#f5d7cc 0%,rgba(245,215,204,0) 70%),linear-gradient(180deg,#efd7d0 0%,#d9b2a8 55%,#b38a80 100%)}
.book-tag{position:absolute;left:88px;top:78px;width:124px;height:40px;background:var(--orange);color:var(--white);font-size:13px;display:flex;align-items:center;justify-content:center}
.program-name{margin-top:18px;font-size:20px;color:var(--orange)}
.program-meta{font-size:14.5px;line-height:23px;color:var(--muted);margin-top:4px}

.banner{left:0;top:1419px;width:1200px;height:415px;background:
  radial-gradient(ellipse 230px 150px at 560px 160px,#a7b39a 0%,rgba(167,179,154,0) 70%),
  radial-gradient(ellipse 200px 140px at 140px 120px,#b7c2ae 0%,rgba(183,194,174,0) 70%),
  radial-gradient(ellipse 200px 140px at 1040px 120px,#b3bea9 0%,rgba(179,190,169,0) 70%),
  radial-gradient(ellipse 190px 110px at 600px 310px,#4a4a4e 0%,rgba(74,74,78,0) 70%),
  linear-gradient(180deg,#dfe3dc 0%,#eef0ec 45%,#f7f7f5 70%,#e4e4e0 100%)}

/* before after */
.ba-title{position:absolute;left:0;top:1880px;width:1200px;text-align:center;font-size:44px}
.client-card{position:absolute;left:77px;top:1971px;width:249px;height:249px;background:linear-gradient(160deg,#58b4e0,#2f8ac4);color:var(--white);text-align:center;padding:34px 16px}
.client-card h3{font-size:22px;font-weight:700;margin-bottom:10px}
.client-card p{font-size:14px;line-height:26px}
.ba{top:1971px;width:250px;height:249px;display:flex}
.ba .half{flex:1;position:relative}
.ba .half + .half{border-left:3px solid #fff}
.ba .before{background:linear-gradient(180deg,#d6cfc8 0%,#2b2a2e 18%,#2b2a2e 28%,#c8957c 32%,#b98268 65%,#3a3438 72%,#28252a 100%)}
.ba .after{background:linear-gradient(180deg,#d9d1c7 0%,#6d8f5c 18%,#c4605a 28%,#c79a80 32%,#b07c63 65%,#7a8f5e 72%,#c8605a 100%)}
.ba .dark{background:linear-gradient(180deg,#c7b6a3 0%,#3f5f9a 20%,#3f5f9a 30%,#c89b80 34%,#b0806a 66%,#2a272b 72%,#222 100%)}
.kg{position:absolute;bottom:10px;width:100%;text-align:center;color:#fff;font-size:18px;letter-spacing:3px}
.arrow{position:absolute;top:2078px}

/* testimonials */
.testimonials{position:absolute;top:2274px;left:0;width:1200px;height:412px;text-align:center;color:var(--white);background:
  radial-gradient(ellipse 160px 200px at 150px 260px,rgba(120,95,85,.55) 0%,rgba(120,95,85,0) 70%),
  radial-gradient(ellipse 160px 200px at 1050px 260px,rgba(130,100,105,.55) 0%,rgba(130,100,105,0) 70%),
  radial-gradient(ellipse 200px 200px at 700px 280px,rgba(110,90,80,.45) 0%,rgba(110,90,80,0) 70%),
  linear-gradient(180deg,#2b2826 0%,#332c28 50%,#1a1716 100%)}
.testimonials .section-title{position:absolute;top:50px;width:100%;font-size:40px}
.quote-badge{position:absolute;left:570px;top:136px;width:60px;height:60px;border-radius:50%;background:var(--blue);font-size:52px;line-height:78px;color:var(--white)}
.quote-text{position:absolute;left:221px;top:222px;width:758px;font-size:15px;line-height:25px}
.quote-name{position:absolute;top:318px;width:100%;font-size:18px;color:var(--orange);font-weight:700}
.quote-role{position:absolute;top:346px;width:100%;font-size:14px;font-style:italic;color:#ccc}

/* booking */
.book-box{position:absolute;left:77px;top:2742px;width:375px;height:376px;background:
  radial-gradient(ellipse 120px 160px at 110px 200px,rgba(255,255,255,.22) 0%,rgba(255,255,255,0) 70%),
  linear-gradient(160deg,#5ab7e2,#2e93cf)}
.book-box h2{position:absolute;top:30px;width:100%;text-align:center;font-family:var(--script);font-weight:400;font-size:48px;line-height:56px;color:var(--white)}
.field{position:absolute;left:33px;width:312px;height:51px;border:1.5px solid rgba(255,255,255,.85);color:var(--white);font-size:15px;padding:15px 20px}
.book-btn{position:absolute;left:33px;top:282px;width:312px;height:54px;background:var(--white);color:var(--orange);font-size:26px;font-weight:700;display:flex;align-items:center;justify-content:center;letter-spacing:1px}

.tips-title{position:absolute;left:522px;top:2740px;font-size:42px}
.tips-lead{position:absolute;left:522px;top:2804px;width:600px;font-size:17px;line-height:29px;color:var(--ink)}
.tips-list{position:absolute;left:522px;top:2895px;width:600px;list-style:none;font-size:14.5px;line-height:24px;color:var(--ink)}
.tips-list li{position:relative;padding-left:20px;margin-bottom:7px}
.tips-list li::before{content:"";position:absolute;left:2px;top:10px;width:5px;height:5px;border-radius:50%;background:var(--blue)}

/* footer */
.site-footer{position:absolute;top:3169px;left:0;width:1200px;height:261px;background:var(--footer-bg)}
.footer-brand{position:absolute;left:77px;top:26px;display:flex;align-items:center;gap:8px}
.footer-brand .brand-name{font-size:36px}
.footer-brand .brand-mark{width:13px;height:13px}
.footer-tag{position:absolute;left:200px;top:66px;font-size:10px;color:var(--muted)}
.footer-rule{position:absolute;left:77px;top:132px;width:226px;height:1px;background:#ccc}
.social{position:absolute;top:154px;width:46px;height:46px;border-radius:50%;background:var(--blue)}
.footer-col{position:absolute;top:32px}
.footer-col h4{font-family:var(--script);font-weight:400;color:var(--orange);font-size:24px;margin-bottom:14px}
.links{list-style:none;font-size:14px;line-height:26px;color:var(--ink)}
.post{display:flex;gap:12px;margin-bottom:14px;width:240px}
.avatar{width:50px;height:50px;border-radius:50%;background:linear-gradient(135deg,#d8b59c,#8c6a52);flex:none}
.post p{font-size:14px;line-height:20px}
.post span{display:block;font-size:11px;font-style:italic;color:var(--orange)}
.online p{font-size:14px;line-height:22px;color:var(--muted);width:240px}
.btn-orange{margin-top:18px;width:142px;height:52px;background:var(--orange);color:var(--white);display:flex;align-items:center;justify-content:center;font-size:17px;font-weight:700}

.bottom-bar{position:absolute;top:3430px;left:0;width:1200px;height:65px;background:var(--orange);color:var(--white);font-size:15px;display:flex;align-items:center;justify-content:center}
</style>
</head>
<body>

<header class="site-header">
  <div class="brand"><span class="brand-mark"></span><span class="brand-name">COREVAIL</span></div>
  <div class="brand-tag">Personal Training Centre</div>
  <nav class="main-nav">
    <a class="active" href="#">Home</a><a href="#">Programs</a><a href="#">Sucess Story</a><a href="#">Community</a><a href="#">Shop</a><a href="#">Blog</a><a href="#">Contact</a>
  </nav>
</header>

<section class="hero">
  <div class="photo hero-photo" role="img" aria-label="Smiling trainer in a yellow top leading a dance fitness class in a bright gym"></div>
  <div class="photo hero-veil"></div>
  <div class="hero-name">Marla Kessing</div>
  <div class="hero-title">Lose FAT be FIT.</div>
  <div class="hero-sub">Get in to the Shape &amp; live the healthy life</div>
  <div class="btn-outline">LET'S GET STARTED</div>
</section>

<section class="about">
  <h2 class="section-title about-title">About Us</h2>
  <p class="about-text">Lorem Ipsum is simply dummy text of the printing and typesetting industry. Lorem Ipsum has been the industry's standard dummy text ever since the 1500s, when an unknown printer took a galley of type and scrambled it to make a type specimen book. It has survived not only five centuries, but also the leap into electronic typesetting, remaining essentially unchanged.</p>
  <div class="btn-blue">READ MORE</div>
  <div class="photo video" role="img" aria-label="Video still of a woman doing a plank in a gym">
    <svg class="play" width="48" height="48" viewBox="0 0 48 48"><circle cx="24" cy="24" r="24" fill="#e62117"/><path d="M19 14 L34 24 L19 34 Z" fill="#fff"/></svg>
  </div>
</section>

<section class="programs">
  <div class="program" style="left:0">
    <div class="photo p1" role="img" aria-label="Group dance fitness class"><div class="book-tag">BOOK NOW</div></div>
    <div class="program-name">Programe Name</div>
    <div class="program-meta">Lorem Ipsum is simply dummy<br>TIME : 6:30 TO 7:30 PM</div>
  </div>
  <div class="program" style="left:300px">
    <div class="photo p2" role="img" aria-label="Aerobics class in a studio"></div>
    <div class="program-name">Programe Name</div>
    <div class="program-meta">Lorem Ipsum is simply dummy<br>TIME : 6:30 TO 7:30 PM</div>
  </div>
  <div class="program" style="left:600px">
    <div class="photo p3" role="img" aria-label="Woman training on gym equipment"></div>
    <div class="program-name">Programe Name</div>
    <div class="program-meta">Lorem Ipsum is simply dummy<br>TIME : 6:30 TO 7:30 PM</div>
  </div>
  <div class="program" style="left:900px">
    <div class="photo p4" role="img" aria-label="Women exercising with fitness balls"></div>
    <div class="program-name">Programe Name</div>
    <div class="program-meta">Lorem Ipsum is simply dummy<br>TIME : 6:30 TO 7:30 PM</div>
  </div>
</section>

<div class="photo banner" role="img" aria-label="Woman holding a balance pose on the floor of a bright room with tall windows"></div>

<section class="transformations">
  <h2 class="section-title ba-title">Before / After Transformation</h2>
  <svg class="arrow" style="left:22px" width="24" height="44" viewBox="0 0 24 44"><path d="M20 2 L4 22 L20 42" fill="none" stroke="#999" stroke-width="2"/></svg>
  <div class="client-card">
    <h3>Client's Name</h3>
    <p>Lorem Ipsum is simply dummy text of the printing and typesetting industry. Lorem Ipsum has been the industry's standard dummy text ever.</p>
  </div>
  <div class="photo ba" style="left:342px" role="img" aria-label="Before and after photos of a client's midsection">
    <div class="half before"><span class="kg">58KG</span></div><div class="half after"><span class="kg">64KG</span></div>
  </div>
  <div class="photo ba" style="left:606px" role="img" aria-label="Before and after photos of a client">
    <div class="half dark"></div><div class="half before"></div>
  </div>
  <div class="photo ba" style="left:869px" role="img" aria-label="Before and after photos of a client's midsection">
    <div class="half before"><span class="kg">58KG</span></div><div class="half after"><span class="kg">64KG</span></div>
  </div>
  <svg class="arrow" style="left:1153px" width="24" height="44" viewBox="0 0 24 44"><path d="M4 2 L20 22 L4 42" fill="none" stroke="#33a6d7" stroke-width="2"/></svg>
</section>

<section class="testimonials" role="img" aria-label="Dim photo of a crowded fitness class behind the testimonial">
  <h2 class="section-title">Testimonials</h2>
  <div class="quote-badge">&ldquo;</div>
  <p class="quote-text">"Lorem Ipsum is simply dummy text of the printing and typesetting industry. Lorem Ipsum has been the industry's standard dummy text ever since the 1500s, when an unknown printer took a galley of type and scrambled it to make a type specimen book."</p>
  <div class="quote-name">JENNA HOLT,</div>
  <div class="quote-role">Head Officer at abc Company</div>
</section>

<section class="booking">
  <div class="book-box" role="img" aria-label="Blue tinted photo of a woman training">
    <h2>Book Your<br>Training</h2>
    <div class="field" style="top:158px">Your Name</div>
    <div class="field" style="top:222px">Your Email Address</div>
    <div class="book-btn">BOOK NOW</div>
  </div>
  <h2 class="section-title tips-title">Tips for Member</h2>
  <p class="tips-lead">Lorem Ipsum is simply dummy text of the printing and typesetting industry. Lorem Ipsum has been the industry's standard dummy text ever since the 1500s.</p>
  <ul class="tips-list">
    <li>Lorem Ipsum is simply dummy text of the printing and typesetting industry. Lorem Ipsum has been the industry's standard dummy text ever since the 1500s.</li>
    <li>Lorem Ipsum is simply dummy text of the printing and typesetting industry.</li>
    <li>Lorem Ipsum is simply dummy text of the printing and typesetting industry.</li>
    <li>Lorem Ipsum is simply dummy text of the printing and typesetting industry. Lorem Ipsum has been the industry's standard dummy text ever since the 1500s.</li>
    <li>Lorem Ipsum is simply dummy text of the printing and typesetting industry. Lorem Ipsum has been the industry's standard dummy text ever since the 1500s.</li>
  </ul>
</section>

<footer class="site-footer">
  <div class="footer-brand"><span class="brand-mark"></span><span class="brand-name">COREVAIL</span></div>
  <div class="footer-tag">Personal Training Centre</div>
  <div class="footer-rule"></div>
  <span class="social" style="left:105px"></span>
  <span class="social" style="left:168px"></span>
  <span class="social" style="left:231px"></span>

  <div class="footer-col" style="left:398px">
    <h4>Useful Links</h4>
    <ul class="links"><li>Home</li><li>About</li><li>New Members</li><li>Conditions</li><li>Contact</li></ul>
  </div>
  <div class="footer-col" style="left:610px">
    <h4>Latest Blog Post</h4>
    <div class="post"><div class="avatar" role="img" aria-label="Blog author thumbnail"></div><p>Lorem Ipsum is simply dummy text of the.<span>12th June, 2016</span></p></div>
    <div class="post"><div class="avatar" role="img" aria-label="Blog author thumbnail"></div><p>Lorem Ipsum is simply dummy text of the.<span>12th June, 2016</span></p></div>
  </div>
  <div class="footer-col online" style="left:874px">
    <h4>Online Programe</h4>
    <p>Visit Our Online Store A Place for All Supplies.</p>
    <div class="btn-orange">VISIT NOW</div>
  </div>
</footer>

<div class="bottom-bar">© COREVAIL - 2017. All Rights Reserved</div>

</body>
</html>
```